Picket Sign Advertising For Alaska Tour Company

I would like a relator style picket sign made that I can place by the water near hotels to generate phone calls and website visits. I want to Advertise Our Daily Jet Boat Tours & Jet Ski Tours. This will be a one sided sign. You may be able to see our past brochure and flyer designs and logo. Our FB page is Harlow Summit Excursions and our website is harlowsummitexcursions.com or contact number is 907-518-4463

```html
<!DOCTYPE html>
<html lang="en">
<head>
<meta charset="utf-8">
<title>Harlow Summit Excursions – Picket Sign</title>
<link rel="stylesheet" href="https://fonts.googleapis.com/css2?family=Anton&family=Cinzel:wght@600&family=Montserrat:wght@600;800&display=swap">
<style>
  :root {
    --page: #e9e7e3;
    --sign-black: #000000;
    --water-deep: #1f3f6e;
    --water-light: #4f7fb4;
    --boat-tone: #7f9a4e;
    --headline-green: #129140;
    --headline-yellow: #ffe11a;
    --headline-red: #ec1c24;
    --burst-blue: #29a8e0;
    --burst-edge: #2e3192;
    --book-red: #ec1c24;
    --phone-yellow: #fff200;
    --brand-gold: #b79d68;
    --tag-white: #f2f2f2;
    --band-cream: #f3edc9;
    --band-text: #111111;
  }
  * { margin: 0; padding: 0; box-sizing: border-box; }
  html, body { width: 1200px; height: 960px; overflow: hidden; background: var(--page); }
  .sign {
    position: absolute; left: 300px; top: 15px; width: 600px; height: 930px;
  }
  .sign-board {
    position: absolute; left: 0; top: 171px; width: 600px; height: 759px;
    background: var(--sign-black);
  }
  .water-photo {
    position: absolute; left: 0; top: 171px; width: 600px; height: 244px;
    background: linear-gradient(180deg, var(--water-light) 0%, var(--water-deep) 60%, #27517f 100%);
  }
  .boats-photo {
    position: absolute; left: 45px; top: 0; width: 550px; height: 245px;
    border-radius: 40px 40px 10px 10px;
    background: linear-gradient(90deg, #b8343a 0%, #3a3f58 35%, var(--boat-tone) 60%, #5f7a3a 100%);
    opacity: 0.9;
  }
  .headline {
    position: absolute; left: 40px; top: 285px; width: 535px; height: 218px;
    background: var(--headline-yellow);
    border: 14px solid var(--headline-red);
    border-radius: 42px;
    display: flex; flex-direction: column; align-items: center; justify-content: center;
    font-family: "Anton", sans-serif; color: var(--headline-green);
    font-size: 76px; line-height: 84px; letter-spacing: 0.5px;
  }
  .book-burst {
    position: absolute; left: 150px; top: 470px; width: 300px; height: 212px;
  }
  .book-text {
    position: absolute; left: 150px; top: 528px; width: 300px; text-align: center;
    font-family: "Anton", sans-serif; color: var(--book-red);
    font-size: 40px; line-height: 42px;
  }
  .phone {
    position: absolute; left: 0; top: 680px; width: 600px; text-align: center;
    font-family: "Anton", sans-serif; color: var(--phone-yellow);
    font-size: 56px; line-height: 70px; letter-spacing: 2px;
  }
  .brand {
    position: absolute; left: 20px; top: 762px; width: 420px;
  }
  .brand-name {
    display: flex; align-items: center; gap: 12px;
    font-family: "Cinzel", serif; font-weight: 600; color: var(--brand-gold);
    font-size: 25px; line-height: 30px;
  }
  .brand-mark { width: 56px; height: 56px; border-radius: 50%; border: 3px solid var(--brand-gold); flex: none; }
  .brand-tagline {
    margin-top: 16px; font-family: "Montserrat", sans-serif; font-weight: 600;
    color: var(--tag-white); font-size: 11px; letter-spacing: 5px;
  }
  .listings {
    position: absolute; left: 448px; top: 778px; width: 145px;
    display: flex; flex-direction: column; gap: 26px; align-items: flex-start;
  }
  .listing {
    display: flex; align-items: center; gap: 8px;
    font-family: "Montserrat", sans-serif; font-weight: 600; font-size: 15px; line-height: 24px;
    color: var(--tag-white); white-space: nowrap;
  }
  .listing-dot { width: 24px; height: 24px; border-radius: 50%; background: var(--tag-white); flex: none; }
  .web-band {
    position: absolute; left: 0; top: 883px; width: 600px; height: 47px;
    background: var(--band-cream);
    display: flex; align-items: center; justify-content: center;
    font-family: "Montserrat", sans-serif; font-weight: 800; color: var(--band-text);
    font-size: 15px; letter-spacing: 6px;
  }
</style>
</head>
<body>
  <main class="sign">
    <div class="sign-board"></div>
    <div class="water-photo" role="img" aria-label="Photo of open blue water"></div>
    <div class="boats-photo" role="img" aria-label="Photo of a red jet ski and a green jet boat with two guides standing aboard"></div>

    <h1 class="headline"><span>Jet Ski Tours</span><span>Jet Boat Tours</span></h1>

    <svg class="book-burst" viewBox="0 0 300 212" aria-hidden="true">
      <polygon points="182,0 185,60 250,50 210,105 300,120 200,135 200,180 150,150 110,212 105,148 40,165 75,118 0,105 90,92 27,17 115,60"
               fill="var(--burst-blue)" stroke="var(--burst-edge)" stroke-width="5" stroke-linejoin="miter"/>
    </svg>
    <p class="book-text">BOOK<br>Now</p>

    <p class="phone">907-518-4463</p>

    <div class="brand">
      <div class="brand-name"><span class="brand-mark"></span><span>Harlow Summit Excursions</span></div>
      <p class="brand-tagline">TAKING YOU WHERE YOU WANT TO GO</p>
    </div>

    <div class="listings">
      <div class="listing"><span class="listing-dot"></span><span>TripNest</span></div>
      <div class="listing"><span class="listing-dot"></span><span>StayHarbor</span></div>
    </div>

    <div class="web-band">harlowsummitexcursions.com</div>
  </main>
</body>
</html>
```